Architectural firm needs a graphic representation of our Master Planning process

We need an image to convey our 3-phase, 8-step Master Planning process that we utilize when designing plans for schools K-12. What we currently use looks very outdated in both the design and color scheme. We'd like an EPS created that can be scaled without distortion. The files I've attached show the current graphic and an instruction sheet which also contains our colors.

```html
<!DOCTYPE html>
<html lang="en">
<head>
<meta charset="utf-8">
<title>Master Planning Process</title>
<link href="https://fonts.googleapis.com/css2?family=Abel&display=swap" rel="stylesheet">
<style>
  :root {
    --page: #ffffff;
    --outline: #d4d4d6;
    --school: #444545;
    --architect: #606165;
    --fundraising: #1c9e78;
    --assess-tone: #939395;
    --problem-tone: #9a9a9c;
    --solutions-tone: #a3a3a5;
    --phase-tone: #b4b4b6;
    --report-tone: #c6c6c8;
    --divider: #c9c9cb;
    --label-light: #f2f2f2;
    --label-dark: #333333;
  }
  html, body {
    margin: 0;
    padding: 0;
    width: 1200px;
    height: 1199px;
    overflow: hidden;
    background: var(--page);
  }
  .process-diagram {
    display: block;
    width: 1200px;
    height: 1199px;
    font-family: "Abel", "Arial Narrow", sans-serif;
  }
  .step-label {
    fill: var(--label-light);
    font-size: 15.5px;
    text-anchor: middle;
  }
  .step-label--spaced { letter-spacing: 4px; font-size: 16px; }
  .legend-label {
    fill: var(--label-dark);
    font-size: 14px;
    text-anchor: middle;
  }
</style>
</head>
<body>
<svg class="process-diagram" viewBox="0 0 1134 1133" xmlns="http://www.w3.org/2000/svg" role="img" aria-label="Three-phase, eight-step master planning process shown as a house">
  <defs>
    <linearGradient id="architect-swatch" x1="0" y1="0" x2="0" y2="1">
      <stop offset="0" stop-color="#3f4044"/>
      <stop offset="1" stop-color="#e2e2e4"/>
    </linearGradient>
  </defs>

  <!-- House outline -->
  <g class="house-outline" fill="var(--outline)" stroke="var(--outline)">
    <rect x="361" y="400" width="412" height="500"/>
    <rect x="655" y="171" width="117" height="200" rx="22" stroke="none"/>
    <polyline points="318,420 567,203 815,420" fill="none" stroke-width="82" stroke-linecap="round" stroke-linejoin="round"/>
  </g>

  <!-- Roof and chimney -->
  <g class="roof" fill="var(--school)">
    <rect x="672" y="188" width="83" height="170" rx="10"/>
    <polyline points="318,420 567,212 815,420" fill="none" stroke="var(--school)" stroke-width="42" stroke-linecap="round" stroke-linejoin="round"/>
    <polygon class="gable" points="378,429 567,272 756,429"/>
  </g>

  <!-- Phase rows -->
  <g class="phase-rows">
    <rect x="378" y="428" width="189" height="92" fill="var(--architect)"/>
    <rect x="567" y="428" width="189" height="92" fill="var(--fundraising)"/>
    <polygon points="548,429 567,417 567,429" fill="var(--architect)"/>
    <polygon points="567,417 586,429 567,429" fill="var(--fundraising)"/>
    <line x1="378" y1="520" x2="756" y2="520" stroke="var(--divider)" stroke-width="1.5"/>

    <rect x="378" y="521" width="126" height="45" fill="var(--architect)"/>
    <rect x="630" y="521" width="126" height="45" fill="var(--fundraising)"/>
    <rect x="504" y="521" width="126" height="45" fill="var(--school)"/>
    <polygon points="547,521 567,508 587,521" fill="var(--school)"/>

    <rect x="378" y="566" width="378" height="90" fill="var(--assess-tone)"/>
    <polygon points="547,566 567,553 587,566" fill="var(--assess-tone)"/>
    <line x1="567" y1="566" x2="567" y2="640" stroke="var(--divider)" stroke-width="1.5"/>

    <rect x="378" y="656" width="378" height="46" fill="var(--problem-tone)"/>
    <polygon points="547,656 567,643 587,656" fill="var(--problem-tone)"/>

    <rect x="378" y="702" width="378" height="46" fill="var(--solutions-tone)"/>
    <polygon points="547,702 567,689 587,702" fill="var(--solutions-tone)"/>

    <rect x="378" y="748" width="126" height="46" fill="var(--phase-tone)"/>
    <rect x="630" y="748" width="126" height="46" fill="var(--fundraising)"/>
    <rect x="504" y="748" width="126" height="46" fill="var(--school)"/>
    <polygon points="547,748 567,735 587,748" fill="var(--school)"/>

    <rect x="378" y="794" width="378" height="45" fill="var(--report-tone)"/>
    <polygon points="547,794 567,781 587,794" fill="var(--report-tone)"/>

    <rect x="378" y="839" width="126" height="45" fill="var(--phase-tone)"/>
    <rect x="630" y="839" width="126" height="45" fill="var(--fundraising)"/>
    <rect x="504" y="839" width="126" height="45" fill="var(--school)"/>
    <polygon points="547,839 567,826 587,839" fill="var(--school)"/>
  </g>

  <!-- Step labels -->
  <g class="step-labels">
    <text class="step-label" x="567" y="380">SCHOOL</text>
    <text class="step-label" x="473" y="473">ARCHITECTURAL</text>
    <text class="step-label" x="473" y="493">CONSULTANT</text>
    <text class="step-label" x="662" y="473">FUND RAISING</text>
    <text class="step-label" x="662" y="493">CONSULTANT</text>
    <text class="step-label step-label--spaced" x="569" y="549">VISIONING</text>
    <text class="step-label" x="473" y="595">PHYSICAL</text>
    <text class="step-label" x="473" y="615">CONDITIONS</text>
    <text class="step-label" x="473" y="636">ASSESSMENT</text>
    <text class="step-label" x="662" y="595">SPACE</text>
    <text class="step-label" x="662" y="615">NEEDS</text>
    <text class="step-label" x="662" y="636">ASSESSMENT</text>
    <text class="step-label" x="567" y="685">PROBLEM DEFINED</text>
    <text class="step-label" x="567" y="731">IDENTIFY SOLUTIONS</text>
    <text class="step-label" x="567" y="776">ASSESS &amp; SELECT</text>
    <text class="step-label" x="567" y="822">COMPILE REPORT</text>
    <text class="step-label" x="567" y="867">IMPLEMENT PLAN !</text>
  </g>

  <!-- Legend -->
  <g class="legend">
    <rect x="403" y="921" width="58" height="18" rx="4" fill="url(#architect-swatch)"/>
    <rect x="538" y="921" width="58" height="18" rx="4" fill="var(--school)"/>
    <rect x="671" y="921" width="58" height="18" rx="4" fill="var(--fundraising)"/>
    <text class="legend-label" x="432" y="958">Architect</text>
    <text class="legend-label" x="567" y="958">School</text>
    <text class="legend-label" x="700" y="958">Fund Raising Consultant</text>
  </g>
</svg>
</body>
</html>
```